Looking to design a new sign for our church.

Looking for a new sign
4 x 8 feet dimension
We are renaming the church "Medlow Ridge Community Church"
looking for legible graphics
Would like some type of backdrop being a family tree (oak) / open to other ideas as you are led
I have included a pic of the old sign for your review
would like to incorporate our Ridge Ministries on the lower right hand corner of the sign / see file attached

```html
<!DOCTYPE html>
<html lang="en">
<head>
<meta charset="utf-8">
<title>Medlow Ridge Community Church – Sign</title>
<link href="https://fonts.googleapis.com/css2?family=Tinos&display=swap" rel="stylesheet">
<style>
  :root {
    --page: #ffffff;
    --sign-navy: #100646;
    --sign-ink: #ffffff;
    --rule: #b9b6cf;
    --tree-tone: #e9e8f0;
  }
  html, body {
    margin: 0;
    padding: 0;
    width: 849px;
    height: 1200px;
    overflow: hidden;
    background: var(--page);
  }
  .canvas {
    position: relative;
    width: 849px;
    height: 1200px;
  }
  .sign {
    position: absolute;
    left: 71px;
    top: 75px;
    width: 708px;
    height: 353px;
    background: var(--sign-navy);
    box-shadow: 6px 7px 8px rgba(0, 0, 0, 0.28);
    font-family: "Tinos", "Times New Roman", serif;
    color: var(--sign-ink);
  }
  .sign-frame {
    position: absolute;
    left: 22px;
    top: 22px;
    width: 664px;
    height: 309px;
    border: 1px solid var(--rule);
    box-sizing: border-box;
  }
  .sign-cross {
    position: absolute;
    left: 37px;
    top: 41px;
    width: 41px;
    height: 64px;
  }
  .welcome {
    position: absolute;
    top: 40px;
    left: 0;
    width: 100%;
    text-align: center;
    font-size: 23px;
    line-height: 1;
    margin: 0;
  }
  .church-name {
    position: absolute;
    top: 72px;
    left: 0;
    width: 100%;
    text-align: center;
    font-size: 72px;
    font-weight: 400;
    line-height: 1;
    margin: 0;
  }
  .church-subtitle {
    position: absolute;
    top: 156px;
    left: 0;
    width: 100%;
    text-align: center;
    font-size: 33px;
    letter-spacing: 1.5px;
    line-height: 1;
    margin: 0;
  }
  .oak-tree {
    position: absolute;
    left: 302px;
    top: 223px;
    width: 103px;
    height: 82px;
    background: radial-gradient(ellipse at 50% 40%, var(--tree-tone) 0%, #cfcde0 100%);
    border-radius: 50% 50% 8% 8% / 60% 60% 8% 8%;
  }
  .ministry-mark {
    position: absolute;
    right: 40px;
    bottom: 46px;
    display: flex;
    align-items: center;
    gap: 5px;
    font-size: 11px;
    line-height: 1.1;
    text-align: right;
  }
  .ministry-dot {
    width: 10px;
    height: 10px;
    border-radius: 50%;
    background: var(--sign-ink);
  }
</style>
</head>
<body>
  <main class="canvas">
    <section class="sign">
      <div class="sign-frame"></div>
      <svg class="sign-cross" viewBox="0 0 41 64" aria-hidden="true">
        <path d="M16 2 H25 V17 H39 V26 H25 V62 H16 V26 H2 V17 H16 Z"
              fill="none" stroke="#ffffff" stroke-width="2.5"/>
        <path d="M18.5 6 H22.5 V20 H35 V23 H22.5 V58 H18.5 V23 H6 V20 H18.5 Z"
              fill="none" stroke="#8f8aa8" stroke-width="1"/>
      </svg>
      <p class="welcome">Welcome To</p>
      <h1 class="church-name">Medlow Ridge</h1>
      <p class="church-subtitle">Community Church</p>
      <div class="oak-tree" role="img" aria-label="White silhouette of a broad family oak tree"></div>
      <div class="ministry-mark">
        <span class="ministry-dot"></span>
        <span>Ridge<br>Ministries</span>
      </div>
    </section>
  </main>
</body>
</html>
```